Basic Webdesign for a Financial Site

That's the design right now:

http://www.kursmodellwerk.com

We want to keep the base design but make it look more modern and professional.

These are Designs we like:

https://www.marktluchs.de/
http://www.verdalino-shop.com/
http://hochkursboerse.de/
http://www.blackwoodcoaching.com/

I use my own WordPress-Theme based on Twitter Bootstrap. I need a PSD and sliced Images (PNG) at the end. Thank you.

Industry/Entity Type

Financial

```html
<!DOCTYPE html>
<html lang="de">
<head>
<meta charset="utf-8">
<title>Kursmodellwerk – Allgemeiner Marktkommentar</title>
<link href="https://fonts.googleapis.com/css2?family=PT+Sans:wght@400;700&family=Arimo:wght@400;700&display=swap" rel="stylesheet">
<style>
:root{
  --page-blue:#2e63a6;
  --page-stripe:#3a6fb2;
  --brand-blue:#1f5ea6;
  --brand-orange:#f29a1f;
  --header-top:#f2f5fa;
  --header-bottom:#dfe7f3;
  --band-blue:#7f9fd3;
  --nav-black:#121212;
  --nav-active:#858585;
  --content-bg:#e9eff8;
  --title-grey:#c9cacc;
  --title-fold:#a9aaac;
  --text-grey:#555a60;
  --panel-grey:#e8e9eb;
  --white:#ffffff;
}
*{box-sizing:border-box;margin:0;padding:0}
html,body{width:1200px;height:1000px;overflow:hidden}
body{
  position:relative;
  font-family:"PT Sans",sans-serif;
  background:repeating-linear-gradient(135deg,var(--page-blue) 0 14px,var(--page-stripe) 14px 22px);
}
.site{
  position:absolute;left:122px;top:31px;width:947px;height:969px;
  background:var(--content-bg);border-radius:10px 10px 0 0;overflow:hidden;
}
.site-header{
  position:absolute;left:0;top:0;width:947px;height:164px;
  background:linear-gradient(var(--header-top),var(--header-bottom));
}
.brand{position:absolute;left:28px;top:40px;display:flex;align-items:center;gap:12px}
.brand-mark{width:46px;height:46px;background:var(--brand-orange)}
.brand-name{font-weight:700;font-size:46px;color:var(--brand-blue);letter-spacing:1px;line-height:1}
.brand-claim{position:absolute;left:25px;top:126px;font-size:25px;font-weight:700;color:var(--brand-blue);letter-spacing:.5px}
.slogan{position:absolute;right:24px;top:135px;font-size:15.5px;font-weight:700;color:var(--brand-blue);letter-spacing:1.2px}
.header-band{position:absolute;left:0;top:164px;width:947px;height:14px;background:var(--band-blue)}
.login{
  position:absolute;left:730px;top:25px;width:230px;height:96px;
  background:var(--panel-grey);border-radius:10px 0 0 10px;
  box-shadow:0 2px 4px rgba(0,0,0,.15);
}
.login-tab{position:absolute;left:0;top:0;width:20px;height:96px;background:#1b1b1b;border-radius:10px 0 0 10px}
.login-tab span{
  position:absolute;left:10px;top:48px;transform:translate(-50%,-50%) rotate(-90deg);
  color:var(--white);font-size:8px;font-weight:700;letter-spacing:1px;white-space:nowrap;
}
.login label{position:absolute;left:38px;font-size:11px;font-weight:700;color:var(--brand-blue)}
.login .field{position:absolute;left:38px;width:155px;height:18px;background:var(--white)}
.login .submit{position:absolute;left:38px;top:76px;font-size:11px;color:var(--brand-blue);letter-spacing:.5px}
.main-nav{position:absolute;left:0;top:178px;width:947px;height:36px;background:var(--nav-black)}
.main-nav a{
  position:absolute;top:0;height:36px;line-height:37px;color:var(--white);
  font-weight:700;font-size:17px;letter-spacing:1px;text-decoration:none;
}
.main-nav a.active{background:var(--nav-active);top:4px;height:29px;line-height:30px;width:103px;text-align:center}
.main-nav .sep{position:absolute;top:8px;width:1px;height:22px;background:var(--white)}
.post-title{
  position:absolute;left:93px;top:239px;width:769px;height:55px;background:var(--title-grey);
  text-align:center;font-family:"Arimo",sans-serif;font-size:21px;font-weight:700;color:var(--text-grey);line-height:58px;
}
.fold{position:absolute;top:294px}
.chart{
  position:absolute;left:118px;top:294px;width:720px;height:399px;
  background:linear-gradient(180deg,#ffffff 0%,#f3f4f6 70%,#e6e7ea 100%);
  border-bottom:16px solid #e4e4e4;
}
.post-body{
  position:absolute;left:119px;top:726px;width:722px;
  font-family:"Arimo",sans-serif;font-weight:700;font-size:10px;line-height:13.4px;
  color:var(--text-grey);text-align:left;
}
.site-footer{position:absolute;left:0;top:922px;width:947px;height:47px;background:var(--nav-black)}
.site-footer nav{position:absolute;left:25px;top:15px;font-family:"Arimo",sans-serif}
.site-footer nav a{color:var(--white);font-size:15px;font-weight:700;text-decoration:none;margin-right:21px;letter-spacing:.4px}
.social{position:absolute;right:26px;top:14px;display:flex;gap:32px}
.social span{display:block;width:20px;height:20px;border-radius:50%;background:var(--white)}
</style>
</head>
<body>
<div class="site">
  <header class="site-header">
    <div class="brand"><div class="brand-mark"></div><div class="brand-name">KURSMODELLWERK</div></div>
    <div class="brand-claim">FÜR DIE PRAXIS</div>
    <div class="slogan">SO SICHERN SIE SICH AN DER BÖRSE EIN REGELMÄẞIGES EINKOMMEN</div>
    <form class="login">
      <div class="login-tab"><span>REGISTRIEREN</span></div>
      <label style="top:9px">Benutzername</label>
      <div class="field" style="top:22px"></div>
      <label style="top:44px">Passwort</label>
      <div class="field" style="top:57px"></div>
      <div class="submit">Anmelden</div>
    </form>
  </header>
  <div class="header-band"></div>
  <nav class="main-nav">
    <a style="left:25px">STARTSEITE</a><i class="sep" style="left:136px"></i>
    <a style="left:167px">ÜBER UNS</a><i class="sep" style="left:272px"></i>
    <a style="left:304px">BUCH</a><i class="sep" style="left:382px"></i>
    <a class="active" style="left:386px">BLOG</a><i class="sep" style="left:494px"></i>
    <a style="left:528px">PRODUKTE</a><i class="sep" style="left:642px"></i>
    <a style="left:674px">COACHING</a><i class="sep" style="left:799px"></i>
    <a style="left:830px">NÜTZLICHES</a>
  </nav>

  <h1 class="post-title">Allgemeiner Marktkommentar 25.09.2013</h1>
  <svg class="fold" style="left:93px" width="26" height="16"><polygon points="0,0 26,0 26,16" fill="var(--title-fold)"/></svg>
  <svg class="fold" style="left:837px" width="26" height="16"><polygon points="0,0 26,0 0,16" fill="var(--title-fold)"/></svg>

  <div class="chart" role="img" aria-label="Kurschart eines Aktienindex im Jahresverlauf mit Anstieg und starkem Einbruch im Herbst"></div>

  <article class="post-body">
    <p>In der abgelaufenen Woche hat sich nicht viel getan. In den Hexensabbat am Freitag hinein, stiegen die Aktienmärkte an und wurden dann, am Freitag abverkauft. Da dies allerdings in vielen Märkten von Allzeithochs oder zumindest Mehrjahreshochs aus geschieht, erscheint uns dies lediglich als Korrektur im Aufwärtstrend. Ein Fehlausbruch kann zwar nicht ausgeschlossen werden, aber dafür müssten sich erst noch niedrigere Hochs bilden und dies ist aktuell nicht zu sehen. Daher sollten wir auch nicht den Kassandrarufen der Crashpropheten allzu viel Aufmerksamkeit widmen. Irgendwann werden auch diese wieder einmal richtig liegen, genau wie eine stehengebliebene Uhr 2x am Tag die richtige Zeit anzeigt. Besser ist es da selbst einen Blick in die Vergangenheit zu werfen und sich beispielsweise das Jahr 1987, welches zuletzt so oft bemüht wird, näher anzuschauen. 1987 stieg der Leitindex vom Jahresanfang bis zum Hoch am 25.08. um fast 40% an. (2013 +23%). Danach fiel der Markt innerhalb von 10 Handelstagen um rund 8,5%, zurück auf seine vorherigen Hochs aus dem Juni und Juli. Dies entsprach einer Korrektur auf das 0,25er Retracement der Aufwärtsbewegung seit September 1986. In den folgenden 4 Handelswochen stieg der Index wieder an und bildete dann am 02.10.1987 ein niedrigeres Hoch aus, welches als solches aber erst nach dem Unterbieten der Tiefs vom September als solche zu erkennen war. Dies geschah am 14.10.1987. Aber auch dann kam es noch nicht zum Crash, sondern erst 2 Handelstage später am Freitag den 16.10.1987 begann dann der eigentliche Crash welcher dann aber bereits 2 Handelstage später am Dienstag den 20.10.1987 mit einer Umkehrkerze endete. Was lernen wir aus diesem kleinen Rückblick in die Vergangenheit? Rückschläge an den Börsen sind jederzeit und quasi aus dem Nichts möglich. Crashartige Einbrüche wie sie derzeit aber an den Märkten beschworen werden sind dagegen (sage niemals nie) extrem unwahrscheinlich in Bezug auf die Aktienmärkte als Ganzes.</p>
  </article>

  <footer class="site-footer">
    <nav><a>Terms and Conditions</a><a>Imprint</a><a>Disclaimer</a><a>Contact Us</a></nav>
    <div class="social"><span aria-label="Soziales Netzwerk"></span><span aria-label="Soziales Netzwerk"></span><span aria-label="Soziales Netzwerk"></span></div>
  </footer>
</div>
</body>
</html>
```